Indonesian Restaurant in Singapore Needs a Menu Design

We need a new menu design for Kedai Rasa 52's Singapore branch. We sell Indonesian fast food; our specialties are ayam penyet set meal (crispy chicken set meal), oxtail soup with rice, beefball soup noodles, chicken noodle special and our famous Kedai Rasa (ice mixed fruit) dessert. We would like pictures of our specialities (and if space and creativity permitting, other photos too) included in our menu with its name below or above it to entice customers to purchase the items. The design colours should include yellow and green and perhaps some red - similar to our logo.
Our current menu is double-sided A4-size with equal-sized photos of some of our food and drinks. We would like the menu to be larger - maybe 25x35cm double-sided or tri-fold.
The feel of our restaurant is casual and personable. The restaurant is located in a downtown mall, thus convenient for customers to visit. Our food is tasty and is served within 5 to 10 minutes. Think BurgerJaya with rice and noodles served, but with personable staff.
Pictures of these food choices are uploaded. Refer to http://www.kedairasa52.example/ for our food choices. Our menu and logo is included in the file titled "Dec 15 Kedai Rasa Order sheet"

Target Market(s)

Our target customers are young people, students, Indonesians and the Malay community in Singapore.

Industry/Entity Type

Asian Restaurant

Font styles to use
Serif
Sans Serif

Requirements
Must have
• Pictures of specialties with its name above or below, yellow and green included in design. Halal logo should be in the menu.
Nice to have
• organised items for menu, with nice headings for each food category, logo included in menu.

```html
<!DOCTYPE html>
<html lang="en">
<head>
<meta charset="utf-8">
<title>Set Meal and Rice Menu</title>
<link rel="stylesheet" href="https://fonts.googleapis.com/css2?family=Cherry+Swash:wght@700&family=Marcellus+SC&family=Arimo:ital,wght@0,700;1,700&display=swap">
<style>
  :root {
    --paper: #efebe8;
    --white: #ffffff;
    --ink: #2a2522;
    --green: #1f6b4a;
    --rice-light: #f2ede4;
    --rice-mid: #d9d0c2;
    --dish-dark: #3b2416;
    --frame: #2b2b2b;
    --chilli: #c8291d;
    --chilli-stem: #4f7a2a;
    --cross: #3a2a22;
  }
  * { margin: 0; padding: 0; box-sizing: border-box; }
  html, body { width: 1200px; height: 713px; overflow: hidden; background: var(--white); }
  .menu-page {
    position: relative; width: 1200px; height: 713px; overflow: hidden;
    background: linear-gradient(to right, var(--white) 0 20px, var(--paper) 20px);
    color: var(--ink);
  }
  .header-strip { position: absolute; left: 20px; top: 0; width: 1180px; height: 110px; }
  .header-title {
    position: absolute; left: 210px; top: 12px;
    font-family: "Marcellus SC", serif; font-size: 35px; letter-spacing: 1px; color: #3a3430;
  }
  .section-banner { position: absolute; }
  .section-banner svg { position: absolute; inset: 0; width: 100%; height: 100%; }
  .section-banner span {
    position: relative; display: block; text-align: center;
    font-family: "Cherry Swash", serif; font-weight: 700; color: var(--white);
    letter-spacing: 2px;
  }
  .banner-set { left: 151px; top: 113px; width: 262px; height: 55px; }
  .banner-set span { font-size: 33px; line-height: 55px; }
  .banner-rice { left: 535px; top: 442px; width: 150px; height: 57px; }
  .banner-rice span { font-size: 35px; line-height: 57px; }
  .set-note {
    position: absolute; left: 173px; top: 178px;
    font-family: "Arimo", sans-serif; font-style: italic; font-weight: 700; font-size: 24px;
  }
  .currency {
    position: absolute; right: 42px;
    font-family: "Arimo", sans-serif; font-weight: 700; font-size: 24px;
  }
  .menu-list { position: absolute; list-style: none; }
  .menu-item {
    position: absolute; left: 0; white-space: nowrap;
    display: flex; align-items: baseline;
  }
  .item-name { font-family: "Marcellus SC", serif; font-size: 28px; letter-spacing: 1px; }
  .item-gloss {
    font-family: "Arimo", sans-serif; font-style: italic; font-weight: 700; font-size: 24px;
  }
  .item-price {
    margin-left: auto; margin-right: 41px;
    font-family: "Arimo", sans-serif; font-weight: 700; font-size: 24px;
  }
  .food-photo {
    position: absolute; left: 20px; top: 402px; width: 467px; height: 311px;
    background: radial-gradient(ellipse at 70% 80%, #8a5428 0%, #5d3a1f 35%, transparent 60%),
                linear-gradient(120deg, #3f6b2c 0%, #5b8a3d 35%, #e9e4da 55%, #c9a27a 100%);
  }
  .spice-mark { position: absolute; width: 34px; height: 46px; }
</style>
</head>
<body>
<main class="menu-page">
  <svg class="header-strip" viewBox="0 0 1180 110" role="img" aria-label="Banner photo of the grilled chicken set meal with rice and a side dish">
    <defs>
      <linearGradient id="riceTone" x1="0" x2="1">
        <stop offset="0" stop-color="#e8e2d8"/><stop offset="0.6" stop-color="#f2ede4"/><stop offset="1" stop-color="#d9d0c2"/>
      </linearGradient>
      <linearGradient id="dishTone" x1="0" x2="1">
        <stop offset="0" stop-color="#8c5a30"/><stop offset="1" stop-color="#3b2416"/>
      </linearGradient>
    </defs>
    <rect x="0" y="0" width="742" height="72" fill="url(#riceTone)"/>
    <path d="M742 0 H1180 V96 C1080 100 980 108 880 104 C820 100 770 90 742 72 Z" fill="url(#dishTone)"/>
    <rect x="943" y="0" width="237" height="94" fill="#2b2b2b"/>
    <rect x="953" y="0" width="220" height="76" fill="#8a6b9a"/>
  </svg>
  <div class="header-title">Ayam Panggang Set Meal</div>

  <div class="section-banner banner-set">
    <svg viewBox="0 0 262 55" preserveAspectRatio="none"><path d="M0 0 H262 L250 27.5 L262 55 H0 L12 27.5 Z" fill="var(--green)"/></svg>
    <span>SET MEAL</span>
  </div>
  <p class="set-note">"Set meals come with soup, rice and a small salad"</p>
  <span class="currency" style="top:176px">$S</span>
  <ul class="menu-list" style="left:181px;top:0;width:1019px;height:400px">
    <li class="menu-item" style="top:222px;width:1019px"><span class="item-name">Fried Fish Set Meal</span><span class="item-price">7.50</span></li>
    <li class="menu-item" style="top:273px;width:1019px"><span class="item-name">Ayam Penyet Set Meal</span><span class="item-gloss" style="margin-left:26px">Crispy Chicken Set Meal</span><span class="item-price">7.00</span></li>
    <li class="menu-item" style="top:325px;width:1019px"><span class="item-name">Ayam Panggang Set Meal</span><span class="item-gloss" style="margin-left:46px">Fried Chicken Set Meal</span><span class="item-price">6.00</span></li>
  </ul>

  <div class="food-photo" role="img" aria-label="Photo of fried fish with a banana-leaf rice cone and sambal dips"></div>

  <div class="section-banner banner-rice">
    <svg viewBox="0 0 150 57" preserveAspectRatio="none"><path d="M0 0 H150 L140 28.5 L150 57 H0 L10 28.5 Z" fill="var(--green)"/></svg>
    <span>RICE</span>
  </div>
  <span class="currency" style="top:465px">$S</span>
  <ul class="menu-list" style="left:562px;top:0;width:638px;height:713px">
    <li class="menu-item" style="top:506px;width:638px"><span class="item-name">Oxtail Soup with Rice</span><span class="item-price">8.00</span></li>
    <li class="menu-item" style="top:558px;width:638px"><span class="item-name">Chicken Curry with Rice</span><span class="item-price">5.50</span></li>
    <li class="menu-item" style="top:608px;width:638px"><span class="item-name">Oxtail Fried Rice</span><span class="item-price">8.00</span></li>
    <li class="menu-item" style="top:660px;width:638px"><span class="item-name">Nasi Goreng</span><span class="item-gloss" style="margin-left:32px">Fried Rice</span><span class="item-price">5.00</span></li>
  </ul>

  <svg class="spice-mark" style="left:918px;top:600px" viewBox="0 0 34 46" role="img" aria-label="Not spicy marker">
    <path d="M10 4 Q12 9 15 11" stroke="var(--chilli-stem)" stroke-width="3" fill="none" stroke-linecap="round"/>
    <path d="M11 11 C18 9 21 16 20 25 C19 34 25 39 32 43 C21 45 12 39 9 30 C7 22 6 14 11 11 Z" fill="var(--chilli)"/>
    <path d="M4 22 L22 40 M22 22 L4 40" stroke="var(--cross)" stroke-width="4" stroke-linecap="round"/>
  </svg>
  <svg class="spice-mark" style="left:988px;top:600px" viewBox="0 0 34 46" role="img" aria-label="Spicy marker">
    <path d="M10 4 Q12 9 15 11" stroke="var(--chilli-stem)" stroke-width="3" fill="none" stroke-linecap="round"/>
    <path d="M11 11 C18 9 21 16 20 25 C19 34 25 39 32 43 C21 45 12 39 9 30 C7 22 6 14 11 11 Z" fill="var(--chilli)"/>
  </svg>
  <svg class="spice-mark" style="left:918px;top:652px" viewBox="0 0 34 46" role="img" aria-label="Not spicy marker">
    <path d="M10 4 Q12 9 15 11" stroke="var(--chilli-stem)" stroke-width="3" fill="none" stroke-linecap="round"/>
    <path d="M11 11 C18 9 21 16 20 25 C19 34 25 39 32 43 C21 45 12 39 9 30 C7 22 6 14 11 11 Z" fill="var(--chilli)"/>
    <path d="M4 22 L22 40 M22 22 L4 40" stroke="var(--cross)" stroke-width="4" stroke-linecap="round"/>
  </svg>
  <svg class="spice-mark" style="left:988px;top:652px" viewBox="0 0 34 46" role="img" aria-label="Spicy marker">
    <path d="M10 4 Q12 9 15 11" stroke="var(--chilli-stem)" stroke-width="3" fill="none" stroke-linecap="round"/>
    <path d="M11 11 C18 9 21 16 20 25 C19 34 25 39 32 43 C21 45 12 39 9 30 C7 22 6 14 11 11 Z" fill="var(--chilli)"/>
  </svg>
</main>
</body>
</html>
```